T&K Grill Website Design Project

T& K Grill AsaderÃa is a fast-casual restaurant that specializes in southern culture, soul food, baby back ribs and bourbon whiskey.
We need a functional and user friendly website design for our customers to be able to explore our menu options, learn about our culture, as well as be able to place and pay for online orders that can be picked up at the nearest restaurant. Benchmarks for our website are www.wheatloafhouse.example, www.verdanbowl.example and www.cortezgreens.example
The site design should also serve as an initial point of contact for prospective franchisees to dig and learn about the brand and business opportunity.
We want customers (consumers and potential franchisees) to be able to experience FIRST THE FOOD, but also the style and culture of our restaurants via the website design. Key elements for this are: soul food (Warm Every Heart), southern culture, friendly service, bluegrass/folk music, bourbon/moonshine/Tennessee whisky, modern butcher-shop design as well as industrial, wood, modern rustic, organic elements. (see restaurant images of tile, concrete, vintage scales, green wall, etc)
We want the website to provide a good overall brand image and also drive participation and sales by via images of our food, by these images being at front and center of the website design. See benchmark websites (Wheatloaf, Cortez Greens, Verdan) for good examples of this.
Other elements to take under consideration for the website design are:
* Illustrative but simple menu
* Hacer un pedido (order online), Loyalty Program and Franquicias sections should have different, separate and easy to see buttons in the homepage.
* Simple, but modern functionality overall for the website.
* Respect colors and elements of the brand (attached some photos and examples)
* Brand Typography included (NAMES OF TYPOGRAPHY: BEBAS, SONGBIRD, CANTER & VAST SHADOW)
Minimum Deliverables: Home Page, Menu and Order Online. 3 pages total.
• More examples can be found at: www.facebook.com/tkgrillasaderia
• Website architecture / Site Map ATTACHED
* More design elements attached.
* Screenshots of some good elements to take under consideration for website functionality and design.
- BEBAS, SONGBRID, CANTER & VAST SHADOW

```html
<!DOCTYPE html>
<html lang="es">
<head>
<meta charset="utf-8">
<title>T&amp;K Grill Asaderia</title>
<link rel="stylesheet" href="https://fonts.googleapis.com/css2?family=Lobster&family=Rye&family=Delius&family=Roboto:wght@400;500&display=swap">
<style>
:root{
  --paper:#efe3cf;
  --cream:#f1e1c8;
  --wine:#7b0a0e;
  --wine-dark:#5e0709;
  --ink:#2a1a12;
  --night:#0e0c0b;
  --text-light:#efe0c2;
  --muted:#b9b2aa;
}
*{box-sizing:border-box;margin:0;padding:0}
html,body{width:881px;height:1200px;overflow:hidden;background:var(--night)}
body{position:relative;font-family:'Roboto',sans-serif}
.header{position:absolute;left:0;top:0;width:881px;height:83px;background:var(--paper);border-top:2px solid var(--wine)}
.nav a{position:absolute;top:38px;font-size:8px;font-weight:500;color:#3a2e26;text-decoration:none;letter-spacing:.2px;transform:translateX(-50%);white-space:nowrap}
.nav a.active{color:#a2161a}
.brand{position:absolute;left:395px;top:12px;width:91px;height:58px;border-radius:50%;background:#1a1412;display:flex;align-items:center;justify-content:center;font-family:'Lobster',cursive;font-size:15px;color:var(--paper)}
.scene{position:absolute;left:0;top:83px;width:881px;height:1011px;background:linear-gradient(180deg,#3a3e48 0%,#2a2a30 28%,#2b211b 45%,#1a1411 65%,#120f0d 100%)}
.scene-glow{position:absolute;left:0;top:83px;width:881px;height:360px;background:radial-gradient(ellipse at 70% 15%,rgba(150,170,200,.35),transparent 55%),radial-gradient(ellipse at 15% 80%,rgba(150,100,60,.35),transparent 50%)}
.hero-title{position:absolute;left:82px;top:252px;font-family:'Lobster',cursive;font-weight:400;font-size:29px;line-height:32px;color:var(--text-light)}
.arrow{position:absolute;top:296px}
.menu{position:absolute;left:82px;top:443px;width:717px}
.menu-head{height:47px;background:var(--wine);color:#f6e9d3;font-family:'Rye',serif;font-size:15px;text-align:center;line-height:47px}
.cards{display:flex}
.card{width:239px;height:294px;position:relative;background:var(--cream);text-align:center}
.card .photo{height:158px}
.card .notch{position:absolute;left:20px;top:146px;width:0;height:0;border-left:15px solid transparent;border-right:15px solid transparent;border-bottom:12px solid var(--cream)}
.card h3{font-family:'Lobster',cursive;font-weight:400;font-size:11.5px;line-height:15px;color:var(--ink);margin:20px 18px 6px}
.card p{font-size:8px;line-height:15px;color:#4a3f37;margin:0 20px}
.card .order{display:block;margin-top:5px;font-family:'Lobster',cursive;font-size:9.5px;color:#8a1014;text-decoration:underline}
.card.featured{background:var(--wine)}
.card.featured .notch{border-bottom-color:var(--wine)}
.card.featured h3{color:#f6e6cc}
.card.featured p{color:#d5a6a0}
.card.featured .order{color:#fff}
.about{position:absolute;left:82px;top:831px;width:717px;height:263px;background:rgba(10,9,9,.75)}
.about-bar{height:7px;background:var(--wine)}
.about-tip{position:absolute;left:351px;top:7px;border-left:8px solid transparent;border-right:8px solid transparent;border-top:7px solid var(--wine)}
.about h2{font-family:'Delius',cursive;font-weight:400;font-size:21px;color:#f2f0ec;text-align:center;margin-top:35px;white-space:nowrap}
.about p.lead{font-size:8px;line-height:19px;color:var(--muted);text-align:center;margin:4px 20px 0}
.features{display:flex;justify-content:space-between;padding:0 19px;margin-top:27px}
.feature{width:190px;height:75px;position:relative;text-align:center;color:var(--muted)}
.feature h4{font-family:'Lobster',cursive;font-weight:400;font-size:15px;color:#f2ece2;margin-top:19px}
.feature span{display:block;font-size:8px;line-height:15px;margin-top:4px}
.feature i{position:absolute;width:12px;height:11px;border-color:#e8e2d8;border-style:solid;border-width:0}
.feature .tl{left:0;top:0;border-left-width:2px;border-top-width:2px}
.feature .tr{right:0;top:0;border-right-width:2px;border-top-width:2px}
.feature .bl{left:0;bottom:0;border-left-width:2px;border-bottom-width:2px}
.feature .br{right:0;bottom:0;border-right-width:2px;border-bottom-width:2px}
.delivery{position:absolute;left:0;top:1094px;width:881px;height:51px;background:var(--wine)}
.delivery .phone{position:absolute;left:82px;top:13px;font-family:'Lobster',cursive;font-size:16px;color:#fff;white-space:nowrap}
.delivery .mail{position:absolute;right:134px;top:19px;font-family:'Lobster',cursive;font-size:8.5px;color:#fff;white-space:nowrap}
.social{position:absolute;top:17px;width:16px;height:16px;border-radius:2px}
.footer{position:absolute;left:0;top:1145px;width:881px;height:55px;background:var(--night)}
.footer .mini-brand{position:absolute;left:82px;top:13px;width:46px;height:30px;border-radius:50%;background:#241c18;display:flex;align-items:center;justify-content:center;font-family:'Lobster',cursive;font-size:8px;color:var(--paper);white-space:nowrap}
.footer .copy{position:absolute;left:133px;top:23px;font-size:8px;color:#b9b0a6;white-space:nowrap}
.footer .links{position:absolute;right:83px;top:23px;font-size:8px;color:#b9b0a6;white-space:nowrap}
</style>
</head>
<body>
<header class="header">
  <nav class="nav">
    <a class="active" style="left:133px">HOME</a>
    <a style="left:225px">NOSOTROS</a>
    <a style="left:314px">MENU</a>
    <a style="left:566px">PROMOCION</a>
    <a style="left:668px">UBICACION</a>
    <a style="left:761px">SEARCH</a>
  </nav>
  <div class="brand">T&amp;K Grill</div>
</header>

<div class="scene" role="img" aria-label="Interior del restaurante con lamparas industriales, pared de ladrillo y barra de madera"></div>
<div class="scene-glow"></div>

<h1 class="hero-title">Duis autem vel eum iriure dolor in<br>hendrerit in vulputate</h1>
<svg class="arrow" style="left:20px" width="14" height="22" viewBox="0 0 14 22"><path d="M11 2 L3 11 L11 20" fill="none" stroke="#8a8a8a" stroke-width="2.5"/></svg>
<svg class="arrow" style="left:847px" width="14" height="22" viewBox="0 0 14 22"><path d="M3 2 L11 11 L3 20" fill="none" stroke="#8a8a8a" stroke-width="2.5"/></svg>

<section class="menu">
  <div class="menu-head">MENU</div>
  <div class="cards">
    <article class="card">
      <div class="photo" role="img" aria-label="Costillas glaseadas con papas fritas y salsa" style="background:linear-gradient(135deg,#3a1e14,#6b4a30 50%,#c9a45a)"></div>
      <span class="notch"></span>
      <h3>Lorem ipsum dolor sit amet, consect etuer adipiscing elit</h3>
      <p>Vivamus vel eros eget magna volutpat sagittis. Nulla faucibus nibh a magna tincidunt accumsan hendrerit nunc facilisis. Curabitur et libero</p>
      <a class="order">ORDER NOW</a>
    </article>
    <article class="card featured">
      <div class="photo" role="img" aria-label="Papa al horno, frijoles y papas fritas" style="background:linear-gradient(135deg,#7a7a78,#b89a4a 50%,#d9a23a)"></div>
      <span class="notch"></span>
      <h3>Ut wisi enim ad minim veniam, quis nostrud exerci tation ullamcorper</h3>
      <p>Vivamus vel eros eget magna volutpat sagittis. Nulla faucibus nibh a magna tincidunt accumsan hendrerit nunc facilisis. Curabitur et libero</p>
      <a class="order">ORDER NOW</a>
    </article>
    <article class="card">
      <div class="photo" role="img" aria-label="Costillar baby back con salsa barbacoa sobre tabla" style="background:linear-gradient(135deg,#a58468,#6a1a14 50%,#8d5a40)"></div>
      <span class="notch"></span>
      <h3>Eodem modo typi, qui nunc nobis videntur parum clari, fiant sollemnes in futurum</h3>
      <p>Vivamus vel eros eget magna volutpat sagittis. Nulla faucibus nibh a magna tincidunt accumsan hendrerit nunc facilisis. Curabitur et libero</p>
      <a class="order">ORDER NOW</a>
    </article>
  </div>
</section>

<section class="about">
  <div class="about-bar"></div>
  <span class="about-tip"></span>
  <h2>Ricas costillitas baby back de T&amp;K Grill Asaderia</h2>
  <p class="lead">Lorem ipsum dolor sit amet, consectetuer adipiscing elit, sed diam nonummy nibh euismod tincidunt ut laoreet dolore magna aliquam erat volutpat. Ut wisi enim ad minim veniam, quis nostrud exerci tation ullamcorper suscipit lobortis nisl ut aliquip ex ea commodo consequat. Duis autem vel eum iriure dolor in hendrerit in vulputate velit esse molestie consequat, vel illum dolore eu feugiat nulla facilisis at vero eros et accumsan et iusto odio dignissim qui blandit praesent luptatum zzril delenit augue duis dolore te feugait nulla facilisi.</p>
  <div class="features">
    <div class="feature"><i class="tl"></i><i class="tr"></i><i class="bl"></i><i class="br"></i>
      <h4>Nuestras Costillitas</h4><span>Estilo baby back con sabor autentico!</span></div>
    <div class="feature"><i class="tl"></i><i class="tr"></i><i class="bl"></i><i class="br"></i>
      <h4>Papas a la Francesa</h4><span>Hechas en casa de papas 100%<br>Sudcalifornianas</span></div>
    <div class="feature"><i class="tl"></i><i class="tr"></i><i class="bl"></i><i class="br"></i>
      <h4>Ensalada Organica</h4><span>Lechuga, arandanos, queso panela y<br>tomate cherry!</span></div>
  </div>
</section>

<div class="delivery">
  <div class="phone">Servicio a Domicilio : 555 014 2290</div>
  <div class="mail">Email : ventas@tkgrill.example</div>
  <span class="social" style="left:757px;background:#3b5a96"></span>
  <span class="social" style="left:783px;background:#2aa3df"></span>
</div>

<footer class="footer">
  <div class="mini-brand">T&amp;K Grill</div>
  <div class="copy">© 2015&nbsp; All rights reserved.</div>
  <div class="links">Privacy Policy &nbsp;|&nbsp; Sitemap</div>
</footer>
</body>
</html>
```